Consulting Firm stationery design

Now that the MakerHive has given us a new logo we'll now need to have all our stationery designed. So we're asking for this community to help us once again.We're looking to get from you Letterheads (Header and Footer, suitable to be applied on a .docx format. Vectors are required but keep this in mind), Envelopes (Front and Back designs, back is not a must but desirable depending on your design), 9"x 12" Pocket Folders (consider design for front and back, also for pockets as well), Business Cards.An elegant design is a must have, mostly for Folders and Envelopes. The idea with this two is to stand out from others when they're handed over. Ideas are welcomed, we were thinking maybe on some texturing simulation for these.Folders will have 3 addresses and contact information. Envelopes will have 1 address and contact information.Brand Manual attached. vendaluxo logo has been copyrighted already. I'm also attaching the current stationary designs (these never got to be out for production but was going to be before we made the brand changes); Pocker folders page 1 to 4 (pages 2 and 4 are the pocket designs), Pages 5 and 6 (6 is the back of the envelope), Pages 7 and 8 (8 is the back of the business card). No letterhead within these designs as it just had the logo and address.

Industry/Entity Type

Business Consultant

Font styles to use
Serif
Sans Serif

Requirements
Must have
• Elegance
Nice to have
• Modern looking out of common

```html
<!DOCTYPE html>
<html lang="en">
<head>
<meta charset="utf-8">
<title>vendaluxo business card</title>
<link href="https://fonts.googleapis.com/css2?family=Poppins:wght@400;500;600&display=swap" rel="stylesheet">
<style>
  :root {
    --backdrop: #2b2b2b;
    --paper: #ffffff;
    --ink: #333333;
    --ink-soft: #555555;
    --brand-blue: #1672a0;
    --link-blue: #1b6ea3;
    --band-dark: #363636;
    --white: #ffffff;
  }
  * { margin: 0; padding: 0; box-sizing: border-box; }
  html, body {
    width: 1200px; height: 960px; overflow: hidden;
    background: var(--backdrop);
    font-family: "Poppins", sans-serif;
  }
  .stage { position: relative; width: 1200px; height: 960px; }
  .card {
    position: absolute; left: 261px; width: 679px; height: 388px;
    box-shadow: 0 6px 18px rgba(0,0,0,0.5);
  }
  .card-front { top: 61px; background: var(--paper); color: var(--ink); }
  .card-back { top: 511px; background: var(--brand-blue); }

  .front-wordmark {
    position: absolute; left: 40px; top: 44px;
    font-size: 44px; font-weight: 500; color: var(--ink);
    letter-spacing: -1px; line-height: 1;
  }
  .front-wordmark .dot {
    display: inline-block; width: 12px; height: 12px; border-radius: 50%;
    background: var(--brand-blue); margin-left: 6px; vertical-align: top;
  }

  .person { position: absolute; left: 37px; top: 166px; width: 330px; }
  .person-name { font-size: 18px; font-weight: 600; color: var(--ink); }
  .person-role { font-size: 15px; font-weight: 400; color: var(--ink-soft); }
  .credentials { font-size: 11.5px; line-height: 14px; color: var(--ink); }
  .contact-lines { margin-top: 8px; font-size: 14px; line-height: 17px; color: var(--ink-soft); }
  .contact-lines b { font-weight: 600; color: var(--ink); }
  .services { margin-top: 9px; font-size: 14px; color: var(--link-blue); }
  .firm-note { margin-top: 9px; font-size: 13.5px; line-height: 17px; color: var(--ink-soft); }

  .office { position: absolute; left: 389px; top: 170px; font-size: 14px; line-height: 17px; color: var(--ink-soft); }
  .office-name { font-weight: 500; color: var(--ink); }
  .office-contact { margin-top: 57px; }
  .office-web { margin-top: 17px; color: var(--link-blue); }

  .back-wordmark {
    position: absolute; left: 0; right: 0; top: 145px;
    text-align: center; font-size: 70px; font-weight: 500;
    color: var(--white); letter-spacing: -2px; line-height: 1;
  }
  .partner-band {
    position: absolute; left: 0; right: 0; top: 320px; height: 35px;
    background: var(--band-dark);
    display: flex; align-items: center; justify-content: space-between;
    padding: 0 48px 0 37px;
  }
  .partner { color: var(--white); font-size: 20px; font-weight: 500; display: flex; align-items: center; gap: 8px; }
  .partner-mark { width: 20px; height: 20px; background: var(--white); }
  .partner-small { font-size: 13px; }
</style>
</head>
<body>
<div class="stage">
  <section class="card card-front">
    <div class="front-wordmark">vendaluxo<span class="dot"></span></div>

    <div class="person">
      <div><span class="person-name">Marco A. Reyes</span> <span class="person-role">| COO &amp; Partner</span></div>
      <div class="credentials">BSc,MScIS, ERP Specialist, Auditor<br>DataAnalytics</div>
      <div class="contact-lines">
        <div><b>D:</b> (809) 555 0142 ext. 201</div>
        <div><b>M:</b> (809) 555 0177</div>
        <div><b>E:</b> marco@vendaluxo.do</div>
      </div>
      <div class="services">Consultancy • Audit • Analytics</div>
      <div class="firm-note">VENDALUXO SRL<br>DR member firm of vendaluxo LLC</div>
    </div>

    <div class="office">
      <div class="office-name">VENDALUXO SRL</div>
      <div>Ceiba Business Center</div>
      <div>Av. Los Almendros 42, Naco</div>
      <div>Santo Domingo, Rep. Dominicana</div>
      <div class="office-contact">(809) 555 0142<br>info@vendaluxo.do</div>
      <div class="office-web">www.vendaluxo.do</div>
    </div>
  </section>

  <section class="card card-back">
    <div class="back-wordmark">vendaluxo</div>
    <div class="partner-band">
      <span class="partner">Nuvio</span>
      <span class="partner"><span class="partner-mark"></span>Quarzo</span>
      <span class="partner partner-small">FinArco</span>
    </div>
  </section>
</div>
</body>
</html>
```